BRM Going Cashless

Hello,
We are a medical office looking to get a flyer created to promote to our patients we will be going "Cashless." Our tagline will be "Cash-Less is Stress-Less"

"Starting in July, to offer you the fastest and most convenient service, we are transitioning to a cashless system. You can now enjoy faster checkout times and greater security with card and contactless payments. More info to come."

I've added two other flyers as sample designs we've used.

Please include logo, addresses, website, phone number

Files to include jpeg, png, pdf (under 5mb), Facebook and Instagram sizing.

Thank you,
Marlo

```html
<!DOCTYPE html>
<html lang="en">
<head>
<meta charset="utf-8">
<title>BRM – Going Cashless</title>
<link rel="stylesheet" href="https://fonts.googleapis.com/css2?family=Great+Vibes&family=Lato:ital,wght@0,400;0,700;0,900;1,400&family=Montserrat:wght@500;800&display=swap">
<style>
  :root {
    --page-bg: #e3e3e3;
    --ink-dark: #2f2f2f;
    --photo-area: #3a3a3a;
    --ink-text: #1f1f1f;
    --teal: #55c0a5;
    --orange: #f3834a;
    --paper: #f6f6f6;
    --white: #ffffff;
  }
  * { box-sizing: border-box; margin: 0; padding: 0; }
  html, body { width: 1200px; height: 1200px; overflow: hidden; background: var(--page-bg); }
  .flyer {
    position: absolute; left: 160px; top: 30px;
    width: 880px; height: 1140px;
    background: var(--ink-dark); overflow: hidden;
    font-family: "Lato", sans-serif; color: var(--ink-text);
  }
  .flyer-shapes { position: absolute; inset: 0; }
  .headline { position: absolute; left: 0; top: 0; width: 880px; height: 240px; }
  .headline-cash { font-family: "Montserrat", sans-serif; font-weight: 500; fill: var(--white); }
  .headline-is { font-family: "Great Vibes", cursive; fill: var(--orange); }
  .headline-stress { font-family: "Montserrat", sans-serif; font-weight: 800; fill: var(--teal); }

  .brand {
    position: absolute; left: 604px; top: 268px;
    display: flex; align-items: center; gap: 14px;
  }
  .brand-dot { width: 34px; height: 34px; border-radius: 50%; background: var(--teal); }
  .brand-name { font-family: "Lato", sans-serif; font-weight: 900; font-size: 58px; color: var(--orange); letter-spacing: 2px; }

  .intro { position: absolute; left: 72px; top: 616px; width: 480px; }
  .intro-lead { font-family: "Great Vibes", cursive; font-size: 54px; color: var(--orange); line-height: 1; }
  .intro-body { margin-top: 8px; font-size: 26px; line-height: 36px; color: var(--ink-text); white-space: nowrap; }
  .intro-body strong { font-weight: 700; color: #000; }

  .more-info {
    position: absolute; left: 0; top: 933px; width: 439px; height: 52px;
    background: var(--teal); border-top-right-radius: 40px;
    padding: 6px 0 0 72px;
    font-style: italic; font-size: 22px; letter-spacing: 3px; color: var(--ink-dark);
  }
  .contact {
    position: absolute; left: 0; top: 974px; width: 569px; height: 166px;
    background: var(--orange); border-top-right-radius: 50px;
    padding: 14px 0 0 72px;
  }
  .contact-title { font-weight: 900; font-size: 29px; color: var(--white); line-height: 1.1; }
  .contact-phone { display: flex; align-items: center; gap: 12px; margin-top: 6px; }
  .contact-phone-number { font-weight: 900; font-size: 48px; color: var(--ink-dark); line-height: 1; }
  .contact-web { font-size: 32px; color: var(--ink-dark); margin-top: 4px; line-height: 1.1; }

  .offices { position: absolute; left: 611px; top: 760px; width: 210px; }
  .offices-pin { display: block; margin-bottom: 12px; }
  .office { padding: 10px 0 12px; border-bottom: 1.5px solid var(--orange); }
  .office:last-child { border-bottom: none; }
  .office-name { font-weight: 700; font-size: 20px; line-height: 1.2; color: var(--orange); }
  .office-name span { color: var(--teal); }
  .office-address { font-size: 15.5px; line-height: 19px; color: var(--ink-text); margin-top: 4px; }
</style>
</head>
<body>
<main class="flyer">
  <svg class="flyer-shapes" width="880" height="1140" viewBox="0 0 880 1140">
    <rect class="payment-photo" role="img" aria-label="Photo: a card payment at a handheld terminal"
      x="0" y="258" width="880" height="370" fill="var(--photo-area)"/>
    <polygon class="torn-edge" fill="var(--teal)"
      points="0,466 20,474 40,481 55,476 70,490 95,492 115,508 135,505 160,522 185,520 205,538 230,545 250,552 275,560 300,574 320,571 345,588 370,592 395,603 420,612 445,620 470,632 495,640 520,652 550,662 575,668 600,680 630,688 660,700 690,708 720,720 750,732 780,742 810,750 840,762 860,770 880,775 880,1140 0,1140"/>
    <polygon class="paper" fill="var(--paper)"
      points="0,490 25,496 45,505 70,512 90,518 110,522 130,532 155,540 180,548 205,556 230,566 255,572 280,584 305,590 330,600 355,608 380,618 410,626 440,640 470,650 500,660 530,672 560,684 590,692 620,704 650,714 680,726 710,734 740,746 770,756 800,770 830,780 860,792 880,800 880,1140 0,1140"/>
  </svg>

  <svg class="headline" viewBox="0 0 880 240" role="heading" aria-level="1" aria-label="Cash-less is stress-less">
    <text class="headline-cash" x="155" y="139" font-size="92" textLength="500" lengthAdjust="spacingAndGlyphs">CASH-LESS</text>
    <text class="headline-is" x="668" y="140" font-size="84">is</text>
    <text class="headline-stress" x="92" y="226" font-size="108" textLength="698" lengthAdjust="spacingAndGlyphs">STRESS-LESS</text>
  </svg>

  <div class="brand">
    <span class="brand-dot"></span>
    <span class="brand-name">BRM</span>
  </div>

  <section class="intro">
    <p class="intro-lead">Starting in July,</p>
    <p class="intro-body">to offer you the fastest and most<br>convenient service, we are transitioning<br>to a cashless system. You can now enjoy<br>faster checkout times and greater<br>security with <strong>card and contactless<br>payments.</strong></p>
  </section>

  <div class="more-info">MORE INFO TO COME.</div>

  <section class="contact">
    <p class="contact-title">CONTACT US TODAY</p>
    <div class="contact-phone">
      <svg width="50" height="50" viewBox="0 0 50 50" aria-hidden="true">
        <circle cx="25" cy="25" r="23" fill="none" stroke="var(--ink-dark)" stroke-width="4"/>
        <path d="M17 13 l5 -1 3 7 -3 3 c2 4 5 7 9 9 l3 -3 7 3 -1 5 c-1 2 -3 3 -5 3 c-12 -2 -20 -10 -22 -22 c0 -2 1 -4 4 -4z" fill="var(--ink-dark)"/>
      </svg>
      <span class="contact-phone-number">(555) 014-2200</span>
    </div>
    <p class="contact-web">www.brmclinic.com</p>
  </section>

  <aside class="offices">
    <svg class="offices-pin" width="33" height="33" viewBox="0 0 33 33" aria-hidden="true">
      <circle cx="16.5" cy="16.5" r="16.5" fill="var(--orange)"/>
      <path d="M16.5 7 a6 6 0 0 1 6 6 c0 5 -6 11 -6 11 s-6 -6 -6 -11 a6 6 0 0 1 6 -6z" fill="none" stroke="var(--white)" stroke-width="1.8"/>
      <circle cx="16.5" cy="13" r="2" fill="var(--white)"/>
    </svg>
    <div class="office">
      <p class="office-name">Northgate <span>Office</span></p>
      <p class="office-address">210 Maple Ridge Dr.<br>Suite 140<br>Northgate, MD 20000</p>
    </div>
    <div class="office">
      <p class="office-name">Riverside <span>Office</span></p>
      <p class="office-address">88 Wellness Way<br>Riverside, WV 20001</p>
    </div>
    <div class="office">
      <p class="office-name">Hillcrest <span>Office</span></p>
      <p class="office-address">4500 Linden Ave.<br>Ste. 305<br>Hillcrest, MD 20002</p>
    </div>
  </aside>
</main>
</body>
</html>
```